Hybrid education and entertainment company needs help with creating dynamic school worksheets

I'm looking for a skilled individual to create a versatile Microsoft Word template for school worksheets for Lessonvaria. Your task will involve:
- Designing a user-friendly and visually appealing template that can be easily customized for various subjects and grade levels.
- Ensuring the template includes sections for titles, instructions, questions, and space for student responses.
- Incorporating consistent formatting and styles to maintain a professional look across all worksheets.
- Adding placeholders for images, graphics, or interactive elements to enhance engagement.
- Testing the template to ensure compatibility and ease of use for educators.
Your work will help streamline the worksheet creation process, making it easier for educators to develop effective and engaging learning materials.

```html
<!DOCTYPE html>
<html lang="en">
<head>
<meta charset="utf-8">
<title>Lessonvaria Worksheet Template, Pages 1 to 7</title>
<link rel="stylesheet" href="https://fonts.googleapis.com/css2?family=Montserrat:wght@200;400;500;700;800&family=Cormorant+Garamond:wght@300;400;500&family=EB+Garamond:wght@400;500&family=Roboto:wght@400&display=swap">
<style>
  :root {
    --stage: #595959;
    --paper: #fdfdf6;
    --white: #ffffff;
    --lavender: #9896a6;
    --sand: #d6cfbd;
    --stone: #c5c6c5;
    --mist: #bfc1c2;
    --navy: #2b3a5a;
    --tan: #b8967a;
    --ink: #2a2a2a;
    --soft-ink: #555555;
    --olive: #a9a878;
    --slate-line: #8fa0b5;
    --deep-teal: #1f3444;
    --rose: #e8a3a3;
    --rose-line: #e07c7c;
  }
  * { margin: 0; padding: 0; box-sizing: border-box; }
  html, body { width: 1200px; height: 2917px; overflow: hidden; background: var(--stage); }
  .canvas { position: relative; width: 1200px; height: 2917px; background: var(--stage); overflow: hidden; font-family: "EB Garamond", serif; color: var(--ink); }

  .page-range { position: absolute; top: 28px; left: 0; width: 1268px; text-align: center; font-family: "Montserrat", sans-serif; font-weight: 200; font-size: 172px; line-height: 1; color: var(--white); letter-spacing: 2px; }

  /* Cover */
  .cover { position: absolute; left: 609px; top: 197px; width: 506px; height: 653px; background: var(--white); overflow: hidden; }
  .cover-band { position: absolute; left: 0; top: 0; width: 138px; height: 100%; background: var(--lavender); }
  .cover-title { position: absolute; left: 160px; top: 48px; font-family: "Montserrat", sans-serif; font-weight: 800; font-size: 31px; line-height: 40px; color: var(--navy); }
  .cover-title .accent { display: block; color: var(--tan); font-weight: 700; letter-spacing: 0.5px; }
  .cover-instructions { position: absolute; left: 163px; top: 140px; width: 300px; font-family: "Montserrat", sans-serif; font-size: 10px; line-height: 15px; color: var(--ink); }
  .cover-image { position: absolute; left: 36px; top: 215px; width: 470px; height: 438px; background: var(--stone); }
  .cover-details { position: absolute; left: 135px; top: 568px; width: 335px; height: 85px; background: var(--sand); font-family: "Montserrat", sans-serif; padding: 20px 22px 0; }
  .cover-details .row { display: flex; }
  .cover-details .cell { font-size: 8.5px; font-weight: 500; color: var(--ink); }
  .cover-details .cell span { display: block; margin-top: 5px; font-weight: 400; color: #7d7a70; }
  .cover-details .cell:nth-child(1) { width: 118px; }
  .cover-details .cell:nth-child(2) { width: 104px; }
  .cover-details .educator { margin-top: 13px; font-size: 8.5px; color: var(--ink); }

  /* Spreads */
  .spread { position: absolute; left: 104px; width: 1011px; height: 653px; background: var(--paper); }
  .spread.plain { background: var(--white); }
  .page { position: absolute; top: 0; width: 505px; height: 100%; }
  .page.left { left: 0; }
  .page.right { left: 506px; }
  .spread::after { content: ""; position: absolute; left: 505px; top: 0; width: 1px; height: 100%; background: rgba(0,0,0,0.03); }

  .running-head { position: absolute; top: 30px; left: 34px; right: 15px; height: 17px; border-bottom: 1px solid var(--olive); font-size: 7.5px; color: var(--ink); }
  .running-head span { position: absolute; top: 0; }
  .running-head .folio { left: 298px; }
  .running-head .school { left: 345px; }
  .running-head .tmpl { left: 412px; }
  .page.right .running-head { left: 34px; right: 10px; }
  .page.right .running-head .folio { left: 294px; }
  .page.right .running-head .school { left: 344px; }
  .page.right .running-head .tmpl { left: 411px; }
  .contents-page .running-head { left: 16px; }
  .contents-page .running-head .title { left: 18px; color: #d8d6e0; }
  .contents-page .running-head .folio { left: 316px; }
  .contents-page .running-head .school { left: 363px; }
  .contents-page .running-head .tmpl { left: 430px; }

  /* Contents */
  .contents-band { position: absolute; left: 0; top: 0; width: 139px; height: 100%; background: var(--lavender); }
  .contents-word { position: absolute; left: 72px; top: 100px; writing-mode: vertical-rl; transform: rotate(180deg); font-family: "Cormorant Garamond", serif; font-weight: 300; font-size: 70px; line-height: 1; color: var(--white); letter-spacing: 1px; }
  .toc-chapter { position: absolute; left: 188px; display: flex; }
  .toc-number { width: 34px; font-family: "Cormorant Garamond", serif; font-size: 36px; line-height: 1; padding-top: 3px; }
  .toc-body { border-left: 1px solid var(--ink); padding-left: 12px; font-family: "Cormorant Garamond", serif; }
  .toc-title { font-size: 15px; line-height: 18px; }
  .toc-desc { font-size: 8px; letter-spacing: 0.6px; color: var(--soft-ink); margin-bottom: 8px; font-family: "EB Garamond", serif; }
  .toc-line { font-size: 11px; line-height: 16.5px; letter-spacing: 0.3px; }
  .toc-line.l1 { padding-left: 18px; }
  .toc-line.l2 { padding-left: 34px; }

  /* Section page */
  .section-title { position: absolute; left: 0; width: 505px; text-align: center; font-family: "Cormorant Garamond", serif; font-size: 28px; font-weight: 400; }
  .section-label { position: absolute; left: 105px; width: 295px; text-align: center; font-family: "Cormorant Garamond", serif; font-size: 14px; padding-bottom: 5px; border-bottom: 1px solid var(--ink); }
  .rule-box { position: absolute; left: 34px; width: 437px; height: 180px; padding: 20px 16px 0 63px; }
  .rule-box.do { background: var(--lavender); color: #eeeef3; }
  .rule-box.dont { background: var(--sand); color: var(--ink); }
  .rule-box::before { content: ""; position: absolute; left: 48px; top: 18px; bottom: 18px; border-left: 1px solid rgba(255,255,255,0.7); }
  .rule-box .mark { position: absolute; left: 15px; width: 18px; height: 18px; }
  .rule-block { margin-bottom: 12px; }
  .rule-block p { font-size: 7px; line-height: 8.5px; }
  .rule-block ul { margin: 4px 0 0 16px; font-size: 6.6px; line-height: 14px; }

  /* Simple title pages */
  .simple-title { position: absolute; left: 0; width: 505px; top: 80px; text-align: center; font-family: "Cormorant Garamond", serif; font-size: 28px; letter-spacing: 1.5px; font-weight: 400; }
  .simple-sub { position: absolute; left: 105px; width: 295px; top: 120px; text-align: center; font-family: "Cormorant Garamond", serif; font-size: 14px; padding-bottom: 5px; border-bottom: 1px solid var(--ink); }
  .intro { position: absolute; left: 34px; top: 167px; width: 437px; text-align: center; font-size: 6.4px; line-height: 9.3px; color: var(--soft-ink); }
  .intro-rule { position: absolute; left: 264px; top: 218px; width: 207px; border-top: 1px solid var(--ink); }
  .column { position: absolute; top: 241px; width: 207px; font-size: 6.2px; line-height: 9.3px; text-align: justify; color: var(--soft-ink); height: 344px; overflow: hidden; }
  .column p + p { margin-top: 9px; }
  .section-ref { position: absolute; right: 34px; top: 605px; font-family: "Cormorant Garamond", serif; font-size: 12px; }

  .card { position: absolute; width: 168px; height: 173px; padding: 28px 12px 0 55px; font-family: "Cormorant Garamond", serif; }
  .card.filled-lavender { background: var(--lavender); color: #e6e5ec; }
  .card.filled-sand { background: var(--sand); }
  .card.outlined { border: 1.5px solid var(--ink); background: var(--white); }
  .card h3 { font-weight: 400; font-size: 15px; margin-bottom: 10px; letter-spacing: 0.4px; }
  .card p { font-family: "EB Garamond", serif; font-size: 6px; line-height: 9.2px; color: inherit; opacity: 0.85; }
  .card p + p { margin-top: 6px; }
  .card .mark { position: absolute; left: 18px; top: 30px; width: 18px; height: 18px; }
  .photo-strip { position: absolute; left: 408px; top: 166px; width: 97px; height: 452px; background: var(--mist); }
  .quote-mark { position: absolute; left: 61px; top: 536px; font-family: "Cormorant Garamond", serif; font-size: 44px; line-height: 1; }
  .quote-text { position: absolute; right: 122px; top: 571px; width: 360px; text-align: right; font-family: "Cormorant Garamond", serif; font-size: 20px; line-height: 24px; letter-spacing: 0.3px; }

  /* Worksheet pages */
  .sheet-head { position: absolute; top: 26px; left: 43px; right: 24px; height: 15px; border-bottom: 1px solid var(--olive); font-size: 7.5px; }
  .sheet-head span { position: absolute; top: 0; }
  .sheet-title { position: absolute; left: 43px; top: 74px; font-family: "Montserrat", sans-serif; font-weight: 500; font-size: 33px; color: var(--deep-teal); letter-spacing: 0.3px; }
  .answer-box { position: absolute; width: 433px; height: 95px; border: 1px solid var(--slate-line); padding: 14px 12px; font-family: "Montserrat", sans-serif; font-size: 9px; color: var(--ink); }
  .choice-row { position: absolute; left: 0; width: 505px; height: 14px; font-family: "Roboto", sans-serif; font-size: 6.5px; color: var(--soft-ink); }
  .choice { position: absolute; top: 0; display: flex; align-items: center; }
  .choice .box { width: 11px; height: 11px; border: 1px solid var(--rose); margin-right: 12px; position: relative; }
  .choice .box svg { position: absolute; left: 1px; top: -3px; }
  .sheet-note { position: absolute; left: 52px; top: 91px; width: 330px; font-family: "Roboto", sans-serif; font-size: 6.6px; line-height: 12px; color: var(--navy); }
  .sheet-note-tick { position: absolute; left: 33px; top: 96px; }
  .sheet-note-rule { position: absolute; left: 52px; top: 123px; width: 23px; border-top: 1.5px solid var(--rose-line); }
</style>
</head>
<body>
<main class="canvas">

  <div class="page-range">1-7</div>

  <!-- Page 1: cover -->
  <section class="cover">
    <div class="cover-band"></div>
    <h1 class="cover-title">Lessonvaria<span class="accent">Worksheet</span></h1>
    <p class="cover-instructions">Instructions for Students:<br>[Type clear instructions here, e.g., 'Read each question carefully and write your answer in the space provided.']</p>
    <div class="cover-image" role="img" aria-label="Cover image placeholder for a worksheet photo or illustration"></div>
    <div class="cover-details">
      <div class="row">
        <div class="cell">Worksheet Title<span>10 August 2025</span></div>
        <div class="cell">Grade Level<span>Type Grade Level</span></div>
        <div class="cell">Subject<span>Subject Name</span></div>
      </div>
      <p class="educator">Educator: Insert Teacher's Name</p>
    </div>
  </section>

  <!-- Pages 2-3 -->
  <section class="spread" style="top:866px;">
    <div class="page left contents-page">
      <div class="contents-band"></div>
      <div class="running-head"><span class="title">Lessonvaria Worksheet</span><span class="folio">02</span><span class="school">School</span><span class="tmpl">Template</span></div>
      <div class="contents-word">CONTENT</div>

      <div class="toc-chapter" style="top:254px;">
        <div class="toc-number">7</div>
        <div class="toc-body">
          <div class="toc-title">Chapter One</div>
          <div class="toc-desc">Quiatur acepuditis etur mil molupta turiatium quundam</div>
          <div class="toc-line l1">1.1 Section&nbsp; 07</div>
          <div class="toc-line l2">1.1.1 Section Page&nbsp; 07</div>
          <div class="toc-line l2">1.1.2 Section Page&nbsp; 07</div>
          <div class="toc-line l1">1.2 Section&nbsp; 07</div>
        </div>
      </div>
      <div class="toc-chapter" style="top:388px;">
        <div class="toc-number">8</div>
        <div class="toc-body">
          <div class="toc-title">Chapter Two</div>
          <div class="toc-desc">Quiatur acepuditis etur mil molupta turiatium</div>
          <div class="toc-line l1">1.1 Section&nbsp; 08</div>
          <div class="toc-line l2">1.1.1 Section Page&nbsp; 08</div>
          <div class="toc-line l2">1.1.2 Section Page&nbsp; 08</div>
          <div class="toc-line l1">1.2 Section&nbsp; 08</div>
        </div>
      </div>
      <div class="toc-chapter" style="top:522px;">
        <div class="toc-number">9</div>
        <div class="toc-body">
          <div class="toc-title">Chapter Three</div>
          <div class="toc-desc">Quiatur acepuditis etur mil molupta turiatium quundam</div>
          <div class="toc-line l1">1.1 Section&nbsp; 09</div>
          <div class="toc-line l2">1.1.1 Section Page&nbsp; 09</div>
          <div class="toc-line l2">1.1.2 Section Page&nbsp; 09</div>
          <div class="toc-line l1">1.2 Section&nbsp; 09</div>
        </div>
      </div>
    </div>

    <div class="page right">
      <div class="running-head"><span class="title">Lessonvaria Worksheet</span><span class="folio">03</span><span class="school">School</span><span class="tmpl">Template</span></div>
      <h2 class="section-title" style="top:78px;">Section Title</h2>
      <div class="section-label" style="top:144px;">instructions for this section</div>

      <div class="rule-box do" style="top:186px;">
        <svg class="mark" style="top:22px;" viewBox="0 0 18 18"><path d="M2 9.5 L7 14.5 L16 3" fill="none" stroke="#fff" stroke-width="2.4"/></svg>
        <svg class="mark" style="top:98px;" viewBox="0 0 18 18"><path d="M2 9.5 L7 14.5 L16 3" fill="none" stroke="#fff" stroke-width="2.4"/></svg>
        <div class="rule-block">
          <p>Read each line carefully and mark the correct answer before moving on to the next part of the page.</p>
          <ul><li>Circle the key words in each question.</li><li>Write your answer in full sentences where asked.</li><li>Check your spelling when you are finished.</li></ul>
        </div>
        <div class="rule-block">
          <p>Read each line carefully and mark the correct answer before moving on to the next part of the page.</p>
          <ul><li>Circle the key words in each question.</li><li>Write your answer in full sentences where asked.</li><li>Check your spelling when you are finished.</li></ul>
        </div>
      </div>

      <div class="section-label" style="top:400px;">instructions for this section</div>

      <div class="rule-box dont" style="top:442px;">
        <svg class="mark" style="top:22px;" viewBox="0 0 18 18"><path d="M3 3 L15 15 M15 3 L3 15" stroke="#fff" stroke-width="2.4"/></svg>
        <svg class="mark" style="top:98px;" viewBox="0 0 18 18"><path d="M3 3 L15 15 M15 3 L3 15" stroke="#fff" stroke-width="2.4"/></svg>
        <div class="rule-block">
          <p>Do not leave any answer blank; if you are unsure, write your best guess in the space given.</p>
          <ul><li>Do not copy answers from a classmate.</li><li>Do not write outside the answer boxes provided.</li><li>Do not rush through the final questions.</li></ul>
        </div>
        <div class="rule-block">
          <p>Do not leave any answer blank; if you are unsure, write your best guess in the space given.</p>
          <ul><li>Do not copy answers from a classmate.</li><li>Do not write outside the answer boxes provided.</li><li>Do not rush through the final questions.</li></ul>
        </div>
      </div>
    </div>
  </section>

  <!-- Pages 4-5 -->
  <section class="spread" style="top:1533px;">
    <div class="page left">
      <div class="running-head"><span class="title">Lessonvaria Worksheet</span><span class="folio">04</span><span class="school">School</span><span class="tmpl">Template</span></div>
      <h2 class="simple-title">A SIMPLE TITLE</h2>
      <div class="simple-sub">A Simple Title Here</div>
      <p class="intro">This page introduces the topic for the lesson. Read the short passage below, then think about the main idea and the details that support it. Underline any new words you find, and be ready to share one question about the text with the class when you have finished reading both columns.</p>
      <div class="intro-rule"></div>
      <div class="column" style="left:34px;">
        <p>Every topic in this worksheet begins with a short reading passage. Take your time and read slowly, pausing at the end of each paragraph to check that you understand what it says. When a word is new to you, look at the sentences around it for clues about its meaning. Try to picture the ideas in your mind as you read, and note any part that surprises you or raises a question you would like to ask your teacher later in the lesson today.</p>
        <p>Every topic in this worksheet begins with a short reading passage. Take your time and read slowly, pausing at the end of each paragraph to check that you understand what it says. When a word is new to you, look at the sentences around it for clues about its meaning. Try to picture the ideas in your mind as you read, and note any part that surprises you or raises a question you would like to ask your teacher later in the lesson today.</p>
        <p>When you reach the end, write one sentence that sums up the passage in your own words. Then compare your sentence with a partner and decide together which details matter most to the main idea of the text.</p>
      </div>
      <div class="column" style="left:264px;">
        <p>Every topic in this worksheet begins with a short reading passage. Take your time and read slowly, pausing at the end of each paragraph to check that you understand what it says. When a word is new to you, look at the sentences around it for clues about its meaning. Try to picture the ideas in your mind as you read, and note any part that surprises you or raises a question you would like to ask your teacher later in the lesson today.</p>
        <p>Every topic in this worksheet begins with a short reading passage. Take your time and read slowly, pausing at the end of each paragraph to check that you understand what it says. When a word is new to you, look at the sentences around it for clues about its meaning. Try to picture the ideas in your mind as you read, and note any part that surprises you or raises a question you would like to ask your teacher later in the lesson today.</p>
        <p>When you reach the end, write one sentence that sums up the passage in your own words. Then compare your sentence with a partner and decide together which details matter most to the main idea of the text.</p>
      </div>
      <div class="section-ref">1.2 Section&nbsp; 09</div>
    </div>

    <div class="page right">
      <div class="running-head"><span class="title">Lessonvaria Worksheet</span><span class="folio">05</span><span class="school">School</span><span class="tmpl">Template</span></div>
      <h2 class="simple-title">A SIMPLE TITLE</h2>
      <div class="simple-sub">A Simple Title Here</div>

      <div class="card filled-lavender" style="left:34px; top:166px;">
        <svg class="mark" viewBox="0 0 18 18"><path d="M2 9.5 L7 14.5 L16 3" fill="none" stroke="#fff" stroke-width="2.4"/></svg>
        <h3>Title One</h3>
        <p>Use this space to explain a key idea in a few short lines, so students can read it quickly and remember it well.</p>
        <p>Add one example to show how it works.</p>
      </div>
      <div class="card outlined" style="left:215px; top:166px;">
        <svg class="mark" viewBox="0 0 18 18"><path d="M3 3 L15 15 M15 3 L3 15" stroke="#8b8a98" stroke-width="2.4"/></svg>
        <h3>Title&nbsp; Two</h3>
        <p>Use this space to explain a key idea in a few short lines, so students can read it quickly and remember it well.</p>
        <p>Add one example to show how it works.</p>
      </div>
      <div class="card outlined" style="left:34px; top:352px;">
        <h3>Title Three</h3>
        <p>Use this space to explain a key idea in a few short lines, so students can read it quickly and remember it well.</p>
        <p>Add one example to show how it works.</p>
      </div>
      <div class="card filled-sand" style="left:215px; top:352px;">
        <svg class="mark" viewBox="0 0 18 18"><path d="M3 3 L15 15 M15 3 L3 15" stroke="#8b8a98" stroke-width="2.4"/></svg>
        <h3>Title Four</h3>
        <p>Use this space to explain a key idea in a few short lines, so students can read it quickly and remember it well.</p>
        <p>Add one example to show how it works.</p>
      </div>

      <div class="photo-strip" role="img" aria-label="Image placeholder for a lesson photo or graphic"></div>
      <div class="quote-mark">&ldquo;</div>
      <p class="quote-text">Oria as dollesti totas et, sinimporit om molup tatusda delenitem</p>
    </div>
  </section>

  <!-- Pages 6-7 -->
  <section class="spread plain" style="top:2198px;">
    <div class="page left">
      <div class="sheet-head"><span style="left:0;">Lessonvaria Worksheet</span><span style="left:285px;">06</span><span style="left:333px;">School</span><span style="left:397px;">Template</span></div>
      <h2 class="sheet-title">Worksheet.</h2>

      <div class="answer-box" style="left:43px; top:153px;">Worksheet 01 :</div>
      <div class="choice-row" style="top:270px;">
        <div class="choice" style="left:43px;"><span class="box"><svg width="10" height="12" viewBox="0 0 10 12"><path d="M1 7 L4 11 L9 1" fill="none" stroke="#444" stroke-width="1"/></svg></span>Cum sociis natoque penatibus et.</div>
        <div class="choice" style="left:204px;"><span class="box"></span>Donec quam felis, ultricies nec.</div>
        <div class="choice" style="left:361px;"><span class="box"></span>Nascetur ridiculus mus.</div>
      </div>

      <div class="answer-box" style="left:43px; top:314px;">Worksheet 02 :</div>
      <div class="choice-row" style="top:430px;">
        <div class="choice" style="left:43px;"><span class="box"></span>Cum sociis natoque penatibus et.</div>
        <div class="choice" style="left:204px;"><span class="box"></span>Donec quam felis, ultricies nec.</div>
        <div class="choice" style="left:361px;"><span class="box"></span>Nascetur ridiculus mus.</div>
      </div>

      <div class="answer-box" style="left:43px; top:462px;">Worksheet 03 :</div>
      <div class="choice-row" style="top:578px;">
        <div class="choice" style="left:43px;"><span class="box"></span>Cum sociis natoque penatibus et.</div>
        <div class="choice" style="left:204px;"><span class="box"></span>Donec quam felis, ultricies nec.</div>
        <div class="choice" style="left:361px;"><span class="box"></span>Nascetur ridiculus mus.</div>
      </div>
    </div>

    <div class="page right">
      <div class="sheet-head" style="left:32px; right:24px;"><span style="left:0;">Lessonvaria Worksheet</span><span style="left:288px;">07</span><span style="left:325px;">School</span><span style="left:384px;">Template</span></div>
      <svg class="sheet-note-tick" width="8" height="10" viewBox="0 0 8 10"><path d="M1 5 L3 9 L7 1" fill="none" stroke="#2b3a5a" stroke-width="0.9"/></svg>
      <p class="sheet-note">Lorem ipsum dolor sit amet, consectetuer adipiscing elit. Aenean commodo ligula eget dolor. Aenean massa. Cum sociis natoque penatibus et magnis dis parturient montes, nascetur ridiculus mus.</p>
      <div class="sheet-note-rule"></div>

      <div class="answer-box" style="left:30px; top:153px;">Worksheet 04 :</div>
      <div class="choice-row" style="top:270px;">
        <div class="choice" style="left:30px;"><span class="box"><svg width="10" height="12" viewBox="0 0 10 12"><path d="M1 7 L4 11 L9 1" fill="none" stroke="#444" stroke-width="1"/></svg></span>Cum sociis natoque penatibus et.</div>
        <div class="choice" style="left:191px;"><span class="box"></span>Donec quam felis, ultricies nec.</div>
        <div class="choice" style="left:348px;"><span class="box"></span>Nascetur ridiculus mus.</div>
      </div>

      <div class="answer-box" style="left:30px; top:314px;">Worksheet 05 :</div>
      <div class="choice-row" style="top:430px;">
        <div class="choice" style="left:30px;"><span class="box"></span>Cum sociis natoque penatibus et.</div>
        <div class="choice" style="left:191px;"><span class="box"></span>Donec quam felis, ultricies nec.</div>
        <div class="choice" style="left:348px;"><span class="box"></span>Nascetur ridiculus mus.</div>
      </div>

      <div class="answer-box" style="left:30px; top:462px;">Worksheet 06 :</div>
      <div class="choice-row" style="top:578px;">
        <div class="choice" style="left:30px;"><span class="box"></span>Cum sociis natoque penatibus et.</div>
        <div class="choice" style="left:191px;"><span class="box"></span>Donec quam felis, ultricies nec.</div>
        <div class="choice" style="left:348px;"><span class="box"></span>Nascetur ridiculus mus.</div>
      </div>
    </div>
  </section>

</main>
</body>
</html>
```